Business card design needed

We are 2 artists starting up a studio by the water in Sydney ...where we can work and display our art...would like the back ground to be Navy and white stripe...nautical...and the name The Paint Hut to be bold and the main wording...not nautical...if possible thought the A for art could be an easel ...ie the capital A using the cross bar as the platform that paint would be circles of colour....would like the main wording in Black but the easel A in colour
Hope u are able to help
thanku Lorna Vesk
as I will be away in a week for 4 weeks could u please send all info to Mira Colbins email....she can contact me and we can go ahead asap....

Artists

THE PAINT HUT

Hallorans Oar House
The Reach..17 Kellaby Rd..Dunrook 2091 Sydney

Mir Colbin..0437819025..miracolbin@mailnest.example
Lorn Vesk...0429573816..lvesk@harborlink.example

```html
<!DOCTYPE html>
<html lang="en">
<head>
<meta charset="utf-8">
<title>The Paint Hut — Business Card</title>
<link rel="stylesheet" href="https://fonts.googleapis.com/css2?family=Open+Sans:wght@700&family=PT+Sans+Narrow:wght@400;700&display=swap">
<style>
  :root {
    --page-bg: #ececec;
    --navy: #22409a;
    --stripe-white: #ffffff;
    --sun-yellow: #fff200;
    --lime: #b3d66a;
    --magenta: #ec1a8c;
    --ink: #000000;
    --paper-text: #ffffff;
  }
  html, body {
    margin: 0;
    padding: 0;
    width: 1200px;
    height: 766px;
    overflow: hidden;
    background: var(--page-bg);
  }
  .business-card {
    position: absolute;
    left: 40px;
    top: 60px;
    width: 1120px;
    height: 645px;
    background: var(--navy);
    overflow: hidden;
    box-shadow: 0 4px 14px rgba(0,0,0,0.18);
  }
  .card-art {
    position: absolute;
    inset: 0;
    width: 1120px;
    height: 645px;
  }
  .studio-name {
    position: absolute;
    left: 300px;
    top: 150px;
    margin: 0;
    font-family: "Open Sans", sans-serif;
    font-weight: 700;
    font-size: 82px;
    line-height: 1;
    color: var(--ink);
    letter-spacing: -0.5px;
    white-space: nowrap;
  }
  .contacts {
    position: absolute;
    left: 352px;
    top: 350px;
    margin: 0;
    font-family: "PT Sans Narrow", sans-serif;
    color: var(--paper-text);
  }
  .contact-line {
    margin: 0 0 16px;
    font-size: 25px;
    line-height: 40px;
    white-space: nowrap;
  }
  .contact-name {
    font-size: 34px;
    text-transform: uppercase;
  }
  .address {
    position: absolute;
    left: 358px;
    top: 508px;
    margin: 0;
    font-family: "PT Sans Narrow", sans-serif;
    font-style: normal;
    font-size: 25px;
    line-height: 37px;
    color: var(--paper-text);
    white-space: nowrap;
  }
</style>
</head>
<body>
  <main class="business-card">
    <svg class="card-art" viewBox="0 0 1120 645" aria-hidden="true">
      <defs>
        <pattern id="nautical-stripes" width="20" height="14" patternUnits="userSpaceOnUse">
          <rect width="20" height="14" fill="var(--stripe-white)"/>
          <rect y="7" width="20" height="5" fill="var(--navy)"/>
        </pattern>
      </defs>
      <circle class="stripe-sail" cx="-13" cy="427" r="333" fill="url(#nautical-stripes)"/>
      <circle class="dot dot-yellow-corner" cx="50" cy="63" r="69" fill="var(--sun-yellow)"/>
      <circle class="dot dot-lime-small" cx="176" cy="79" r="28" fill="var(--lime)"/>
      <circle class="dot dot-lime-large" cx="980" cy="356" r="84" fill="var(--lime)"/>
      <circle class="dot dot-magenta" cx="904" cy="509" r="52" fill="var(--magenta)"/>
      <circle class="dot dot-yellow-edge" cx="1062" cy="515" r="72" fill="var(--sun-yellow)"/>
    </svg>

    <h1 class="studio-name">The Paint Hut</h1>

    <div class="contacts">
      <p class="contact-line"><span class="contact-name">Colbin</span> : 0437819025 | miracolbin@mailnest.example</p>
      <p class="contact-line"><span class="contact-name">Lorn Vesk</span> : 0429573816 | lvesk@harborlink.example</p>
    </div>

    <address class="address">
      Hallorans Oar House, The Reach..17<br>
      Kellaby Rd. Dunrook 2091, Sydney Lorn
    </address>
  </main>
</body>
</html>
```